One page (Bach and front) flyer graphic composition with all content provided

We need, by Sunday evening at the latest term, to have the enclosed page graphically worked. It will be inserted in a Fair Catalog. Dimensions 20x20We enclose logo and picture to include and draft. Don't consider the Power Point we include only to handle you content: take it from here and decide how to paste it in page to your own judgment.DLW is a software company, producing for investment market. image to give: SERIOUS, COMPETENT, STRAIGHT TO THE POINT and, most important, CREDIBLE company

Target Market(s)

Investors

Font styles to use
Serif

Colors
276eb1
0355a3
ffffff

Requirements
Must have
• Clear, strong Logo in the front page
• The picture on the back
Nice to have
• Credibility, space, clearness
Should not have
• Confusion, too much "loud"

```html
<!DOCTYPE html>
<html lang="en">
<head>
<meta charset="utf-8">
<title>DLW Fair Catalog Flyer</title>
<link rel="stylesheet" href="https://fonts.googleapis.com/css2?family=Montserrat:wght@400;500;600;700&family=Oswald:wght@700&display=swap">
<style>
  :root {
    --blue: #276eb1;
    --blue-deep: #0355a3;
    --blue-band: #1670c0;
    --white: #ffffff;
    --ink: #1d1d1d;
    --grey-head: #4f5356;
    --grey-soft: #5b5f63;
    --stage: #d9dbdd;
    --night: #05070b;
  }
  * { box-sizing: border-box; margin: 0; padding: 0; }
  html, body { width: 1200px; height: 841px; overflow: hidden; }
  body { background: var(--stage); font-family: "Montserrat", sans-serif; position: relative; }

  .page { position: absolute; top: 34px; width: 552px; height: 774px; overflow: hidden; }
  .page--front { left: 34px; background: var(--white); }
  .page--back { left: 614px; background: var(--blue-band); }

  .brand { position: absolute; left: 26px; top: 28px; display: flex; align-items: center; gap: 10px; }
  .brand__dot { width: 56px; height: 56px; border-radius: 50%; background: var(--blue); }
  .brand__name { font-weight: 700; font-size: 52px; line-height: 1; color: var(--blue); letter-spacing: 1px; }
  .brand__tag { position: absolute; left: 106px; top: 92px; font-size: 10px; font-weight: 500; letter-spacing: 1.4px; color: var(--blue-deep); }

  .headline { position: absolute; left: 34px; top: 108px; font-family: "Oswald", sans-serif; font-weight: 700;
    font-size: 50px; line-height: 56px; color: var(--grey-head); }

  .hero-ring { position: absolute; left: 230px; top: 26px; }
  .hero-photo { position: absolute; left: 246px; top: 42px; width: 268px; height: 268px; border-radius: 50%;
    background: radial-gradient(circle at 45% 30%, #5a7fa8 0%, #3a4f66 40%, #a07a52 75%, #d7b488 100%); }

  .centered { position: absolute; transform: translateX(-50%); text-align: center; white-space: nowrap; }
  .pillar-icon { position: absolute; transform: translateX(-50%); top: 292px; }
  .pillar-title { top: 352px; font-weight: 700; font-size: 14px; line-height: 18px; color: var(--grey-soft); letter-spacing: .5px; }
  .pillar-text { font-size: 10.8px; line-height: 13px; color: var(--ink); }
  .pillar-text--need { left: 85px; top: 379px; }
  .pillar-text--problem { left: 256px; top: 372px; }

  .solution-label { position: absolute; left: 26px; top: 496px; font-size: 20px; font-weight: 500; color: var(--grey-soft); white-space: nowrap; }
  .solution-label small { font-size: 16px; letter-spacing: .5px; }

  .solution-frame { position: absolute; left: 0; top: 0; }
  .tile { position: absolute; top: 442px; height: 52px; border-radius: 8px; background: var(--night);
    color: #3e8fe0; font-size: 11px; line-height: 13px; text-align: center; white-space: nowrap;
    display: flex; align-items: center; justify-content: center; }
  .tile--systems { left: 194px; width: 125px; }
  .tile--index { left: 348px; width: 163px; }
  .tile-plus { position: absolute; left: 325px; top: 450px; color: var(--blue); font-size: 26px; font-weight: 500; }

  .system { left: 352px; top: 507px; color: var(--blue-deep); font-size: 11px; line-height: 13.5px; }
  .system__name { font-weight: 700; font-size: 13px; line-height: 14px; }
  .system__full { font-weight: 600; }

  .benefits-title { position: absolute; left: 0; width: 552px; top: 578px; text-align: center; font-size: 22px; font-weight: 500; color: var(--grey-head); }

  .benefits { position: absolute; left: 25px; top: 616px; width: 501px; height: 109px; border-radius: 6px; background: var(--blue-band); color: var(--white); }
  .benefit__name { position: absolute; left: 15px; font-weight: 700; font-size: 16px; line-height: 20px; white-space: nowrap; }
  .benefit__text { font-size: 10.4px; line-height: 13px; }
  .chev { position: absolute; }

  .visit { position: absolute; left: 0; width: 100%; text-align: center; font-size: 13px; letter-spacing: 3px; font-weight: 500; }
  .page--front .visit { top: 737px; color: var(--blue-deep); }

  .back-photo { position: absolute; left: 0; top: 0; width: 552px; height: 555px;
    background: radial-gradient(ellipse at 60% 35%, #3a3320 0%, #14130e 30%, #030406 70%); }
  .back-rule { position: absolute; left: 0; top: 555px; width: 552px; height: 3px; background: var(--white); }
  .back-title { position: absolute; left: 0; width: 100%; top: 590px; text-align: center; color: var(--white); font-size: 37px; font-weight: 700; white-space: nowrap; }
  .back-invite { position: absolute; left: 0; width: 100%; top: 648px; text-align: center; color: var(--white); font-size: 13.5px; line-height: 16px; font-weight: 500; white-space: nowrap; }
  .page--back .visit { top: 720px; color: var(--white); }
</style>
</head>
<body>
  <section class="page page--front">
    <div class="brand">
      <span class="brand__dot"></span>
      <span class="brand__name">DLW</span>
    </div>
    <div class="brand__tag">DataLedgerWorks</div>

    <h1 class="headline">Your<br>Money<br>Growth</h1>

    <svg class="hero-ring" width="300" height="300" viewBox="0 0 300 300">
      <circle cx="150" cy="150" r="142" fill="none" stroke="var(--blue)" stroke-width="5"/>
      <path d="M150 2 A148 148 0 0 1 298 150" fill="none" stroke="var(--blue)" stroke-width="1"/>
      <path d="M270 60 A160 160 0 0 1 260 260" fill="none" stroke="var(--blue)" stroke-width="1"/>
    </svg>
    <div class="hero-photo" role="img" aria-label="Photo of stacked coins on a desk with hands typing on a laptop"></div>

    <svg class="pillar-icon" style="left:85px" width="56" height="56" viewBox="0 0 56 56">
      <circle cx="28" cy="28" r="26" fill="none" stroke="var(--blue)" stroke-width="2.5"/>
      <circle cx="28" cy="26" r="5" fill="var(--blue)"/>
      <path d="M18 42 Q28 30 38 42 Z" fill="var(--blue)"/>
      <circle cx="19" cy="30" r="3.5" fill="var(--blue)"/>
      <circle cx="37" cy="30" r="3.5" fill="var(--blue)"/>
      <rect x="30" y="12" width="12" height="7" fill="none" stroke="var(--blue)" stroke-width="1.6"/>
    </svg>
    <div class="centered pillar-title" style="left:85px">NEED</div>
    <p class="centered pillar-text pillar-text--need">Most of us would<br>prefer a major return<br>on our investments.</p>

    <svg class="pillar-icon" style="left:256px" width="56" height="56" viewBox="0 0 56 56">
      <circle cx="28" cy="28" r="26" fill="none" stroke="var(--blue)" stroke-width="2.5"/>
      <circle cx="30" cy="18" r="5" fill="var(--blue)"/>
      <path d="M22 42 L24 28 Q30 22 36 28 L36 42 Z" fill="var(--blue)"/>
      <path d="M25 34 L29 38 L35 30" fill="none" stroke="var(--white)" stroke-width="2"/>
    </svg>
    <div class="centered pillar-title" style="left:256px">PROBLEM</div>
    <p class="centered pillar-text pillar-text--problem">Most of us lacks instruments,<br>know-how and time to do it by<br>ourselevs. Moreover, extranal aid<br>has often been disappointing.</p>

    <div class="solution-label">DLW <small>SOLUTION</small></div>

    <svg class="solution-frame" width="552" height="774" viewBox="0 0 552 774">
      <path d="M181 464 V558 H522 V464" fill="none" stroke="var(--grey-soft)" stroke-width="1.4"/>
      <circle cx="181" cy="464" r="3.5" fill="var(--blue)"/>
      <circle cx="522" cy="464" r="3.5" fill="var(--blue)"/>
    </svg>
    <div class="tile tile--systems">utilize most efficient<br>and tested trading<br>systems</div>
    <div class="tile-plus">+</div>
    <div class="tile tile--index">Adding its own sentiment<br>index created for first time<br>on blockchain</div>

    <div class="centered system">
      <div class="system__name">ATLAS</div>
      <div class="system__full">Highly Advanced Trading System</div>
      <div>offers major results with a turnkey solution</div>
    </div>

    <h2 class="benefits-title">With ATLAS you can have</h2>

    <div class="benefits">
      <span class="benefit__name" style="top:10px">Better ROI</span>
      <svg class="chev" style="left:114px;top:12px" width="30" height="16" viewBox="0 0 30 16"><path d="M2 2 L10 8 L2 14 M14 2 L22 8 L14 14" fill="none" stroke="#fff" stroke-width="3.5"/></svg>
      <span class="centered benefit__text" style="left:206px;top:7px">TODAY machines work<br>better than humans</span>
      <svg class="chev" style="left:275px;top:12px" width="30" height="16" viewBox="0 0 30 16"><path d="M2 2 L10 8 L2 14 M14 2 L22 8 L14 14" fill="none" stroke="#fff" stroke-width="3.5"/></svg>
      <span class="centered benefit__text" style="left:398px;top:7px">ANUHOW, DLW maintains<br>Human Control OVER machines</span>

      <span class="benefit__name" style="top:42px">Better vision</span>
      <svg class="chev" style="left:131px;top:44px" width="30" height="16" viewBox="0 0 30 16"><path d="M2 2 L10 8 L2 14 M14 2 L22 8 L14 14" fill="none" stroke="#fff" stroke-width="3.5"/></svg>
      <span class="centered benefit__text" style="left:236px;top:39px">Sentimen index finds out<br>what people REALLY thinks</span>
      <svg class="chev" style="left:319px;top:44px" width="30" height="16" viewBox="0 0 30 16"><path d="M2 2 L10 8 L2 14 M14 2 L22 8 L14 14" fill="none" stroke="#fff" stroke-width="3.5"/></svg>
      <span class="centered benefit__text" style="left:414px;top:39px">Sentiment + Data =<br>Unbeatable know how</span>

      <span class="benefit__name" style="top:77px">Miior risk</span>
      <svg class="chev" style="left:105px;top:79px" width="30" height="16" viewBox="0 0 30 16"><path d="M2 2 L10 8 L2 14 M14 2 L22 8 L14 14" fill="none" stroke="#fff" stroke-width="3.5"/></svg>
      <span class="centered benefit__text" style="left:214px;top:74px">ATLAS is founded on proven,<br>real numbers</span>
      <svg class="chev" style="left:298px;top:79px" width="30" height="16" viewBox="0 0 30 16"><path d="M2 2 L10 8 L2 14 M14 2 L22 8 L14 14" fill="none" stroke="#fff" stroke-width="3.5"/></svg>
      <span class="centered benefit__text" style="left:409px;top:74px">Risk and return are<br>known before, not after</span>
    </div>

    <div class="visit">Visit us www.dlwsys.io</div>
  </section>

  <section class="page page--back">
    <div class="back-photo" role="img" aria-label="Photo of a martini glass filled with gold coins and ice cubes on a black background"></div>
    <div class="back-rule"></div>
    <h2 class="back-title">We are waiting for you!</h2>
    <p class="back-invite">Ask your invitation to our DLW Hostess and be welcommed to:<br>Presidential Suite Level 18</p>
    <div class="visit">Visit us www.dlwsys.io</div>
  </section>
</body>
</html>
```